Real Estate Company Needs Business Card Designed

We need a business card design for a new real estate company based in Lakemont, CA (Bay Region North). We plan to improve the residential real estate industry by using technology to improve customer experience. We would like to see designs that use a black background. The final design should communicate sophistication and customer service, as well as stability and technology.

Industry/Entity Type

Real Estate

Requirements
Must have
• Black background

```html
<!DOCTYPE html>
<html lang="en">
<head>
<meta charset="utf-8">
<title>Veltora Business Card</title>
<link rel="stylesheet" href="https://fonts.googleapis.com/css2?family=Jost:wght@400;500&display=swap">
<style>
  :root {
    --backdrop: #5e5f61;
    --card: #1c1a1b;
    --brand: #8fa9dd;
    --ink-light: #f2f2f2;
    --ink-soft: #c9c9c9;
    --ink-muted: #9a9a9a;
    --icon: #6d6d6d;
  }
  * { margin: 0; padding: 0; box-sizing: border-box; }
  html, body { width: 1200px; height: 1028px; overflow: hidden; }
  body {
    background: var(--backdrop);
    font-family: "Jost", "Futura", sans-serif;
    position: relative;
  }
  .business-card {
    position: absolute;
    left: 62px; top: 170px;
    width: 1060px; height: 622px;
    background: var(--card);
    box-shadow: 0 6px 18px rgba(0,0,0,0.45);
  }
  .brand-name {
    position: absolute;
    left: 0; right: 0; top: 80px;
    text-align: center;
    font-weight: 500;
    font-size: 136px;
    line-height: 1;
    letter-spacing: 28px;
    padding-left: 28px;
    color: var(--brand);
  }
  .holder {
    position: absolute;
    left: 0; right: 0; top: 276px;
    text-align: center;
    color: var(--ink-light);
    font-weight: 400;
  }
  .holder-name { font-size: 32px; letter-spacing: 3px; line-height: 40px; }
  .holder-role { font-size: 31px; letter-spacing: 5px; line-height: 52px; padding-left: 5px; }
  .contact-list {
    position: absolute;
    left: 46px; top: 424px;
    list-style: none;
  }
  .contact-item {
    display: flex; align-items: center;
    height: 41px;
    font-size: 23px; letter-spacing: 1.8px;
    color: var(--ink-muted);
  }
  .contact-icon { width: 34px; height: 26px; margin-right: 18px; flex: none; }
  .office {
    position: absolute;
    left: 662px; top: 424px;
    font-size: 23px; letter-spacing: 1.6px;
    line-height: 41px;
    font-style: normal;
    color: var(--ink-soft);
  }
  .office-brand { color: var(--brand); font-weight: 400; }
</style>
</head>
<body>
  <section class="business-card">
    <div class="brand-name">VELTORA</div>

    <div class="holder">
      <div class="holder-name">DANIEL REYES</div>
      <div class="holder-role">Director</div>
    </div>

    <ul class="contact-list">
      <li class="contact-item">
        <svg class="contact-icon" viewBox="0 0 34 26" aria-hidden="true">
          <rect x="11" y="0" width="13" height="26" rx="2" fill="none" stroke="var(--icon)" stroke-width="1.6"/>
          <line x1="15" y1="22.5" x2="20" y2="22.5" stroke="var(--icon)" stroke-width="1.6"/>
        </svg>
        0100 555 014
      </li>
      <li class="contact-item">
        <svg class="contact-icon" viewBox="0 0 34 26" aria-hidden="true">
          <rect x="2" y="4" width="30" height="18" fill="none" stroke="var(--icon)" stroke-width="1.6"/>
          <polyline points="2,4 17,15 32,4" fill="none" stroke="var(--icon)" stroke-width="1.6"/>
        </svg>
        danielreyes@veltora.com
      </li>
      <li class="contact-item">
        <svg class="contact-icon" viewBox="0 0 34 26" aria-hidden="true">
          <circle cx="17" cy="13" r="9" fill="none" stroke="var(--icon)" stroke-width="1.6"/>
          <ellipse cx="17" cy="13" rx="4" ry="9" fill="none" stroke="var(--icon)" stroke-width="1.2"/>
          <line x1="8" y1="13" x2="26" y2="13" stroke="var(--icon)" stroke-width="1.2"/>
        </svg>
        www.veltora.com
      </li>
    </ul>

    <address class="office">
      <div><span class="office-brand">VELTORA</span> company:</div>
      <div>2400 Example Street,</div>
      <div>Lakemont, CA (Bay Region North)</div>
    </address>
  </section>
</body>
</html>
```